www.morvalpastime.com

Updating website so looks futristic but yet business like and easy to navigate, essentially a good landing page with a cool picture summing up what we do, and links to the following pages, all other pages on site to be updated, Exclusive Distributor of Brisk Rig Unique Fitness Equipment Products in UK & Ireland, www.ridgesurge.co.uk Exclusive Partners & Distributors Of Ridge Surge - Obstacle Races - Obstacle Hire - Obstacle Training - Adventure Events, www.trekvaliant.co.uk Adventures That Inspire. We also Health Club / Facillity Consultancy

```html
<!DOCTYPE html>
<html lang="en">
<head>
<meta charset="utf-8">
<title>Morval Pastime – Health, Wellness, Fitness, Consultants</title>
<link href="https://fonts.googleapis.com/css2?family=Cinzel:wght@400;700&family=Open+Sans:wght@400;600;700&display=swap" rel="stylesheet">
<style>
:root{
  --green-dark:#1e4a0c;
  --green:#2f6812;
  --green-mid:#3f8a18;
  --green-light:#c8e79a;
  --slate:#373b40;
  --grey-bar:#77797c;
  --ink:#222;
  --muted:#666;
  --white:#fff;
  --footer:#1c4409;
  --footer-dark:#133306;
}
*{box-sizing:border-box;margin:0;padding:0}
html,body{width:1200px;height:5042px;overflow:hidden}
body{font-family:"Open Sans",Arial,sans-serif;color:var(--ink);background:var(--white);font-size:15px}
a{color:inherit;text-decoration:none}
.photo{display:block}

/* Hero */
.hero{position:relative;height:690px;overflow:hidden}
.hero-photo{position:absolute;inset:0;background:
  radial-gradient(ellipse 260px 340px at 170px 360px,rgba(236,226,160,.75),transparent 70%),
  radial-gradient(ellipse 240px 330px at 1020px 330px,rgba(238,214,60,.7),transparent 70%),
  radial-gradient(ellipse 420px 200px at 600px 640px,rgba(180,120,70,.55),transparent 75%),
  linear-gradient(180deg,#e9ecee 0%,#b9bcbc 22%,#8e8a82 48%,#6d655a 70%,#a77d4e 100%)}
.site-header{position:absolute;top:0;left:0;right:0;height:118px;background:rgba(10,14,8,.78);display:flex;align-items:center;justify-content:space-between;padding:0 70px 0 90px}
.brand-name{font-family:"Cinzel",Georgia,serif;font-size:30px;color:var(--white);white-space:nowrap}
.brand-tag{font-family:"Cinzel",Georgia,serif;font-size:13px;color:#e6e6e6;margin-top:4px;white-space:nowrap}
.main-nav{display:flex;gap:4px}
.main-nav a{color:var(--white);font-size:15px;padding:8px 10px;border:2px solid transparent;white-space:nowrap}
.main-nav a.active{border-color:var(--white)}
.hero-panel{position:absolute;left:330px;top:238px;width:540px;height:318px;background:rgba(12,12,12,.8);border:2px solid rgba(255,255,255,.45);text-align:center;color:var(--white);padding-top:34px}
.hero-kicker{font-family:"Cinzel",Georgia,serif;font-size:16px;font-weight:700;display:flex;justify-content:center;align-items:center;gap:14px}
.hero-title{font-family:"Cinzel",Georgia,serif;font-size:44px;font-weight:400;margin:22px 0 16px}
.hero-text{font-size:14px;line-height:1.5;width:290px;margin:0 auto}
.btn-contact{display:inline-block;margin-top:24px;background:var(--white);color:var(--ink);font-family:"Cinzel",Georgia,serif;font-size:17px;padding:14px 30px}

/* About */
.about{height:402px;background:var(--green-dark);color:var(--white);padding:66px 80px 0}
.about h2{font-family:"Cinzel",Georgia,serif;font-size:36px;font-weight:400}
.about-body{display:flex;gap:22px;margin-top:24px}
.about-photo{width:202px;height:198px;flex:none;border:4px solid var(--white);background:
  radial-gradient(circle at 50% 45%,#d8b79a 0,#b88e70 28%,transparent 42%),
  linear-gradient(160deg,#aab6bc,#5d6a70 55%,#2a3034)}
.about-name{font-family:"Cinzel",Georgia,serif;font-size:22px}
.about-role{font-size:14px;margin:4px 0 16px}
.about-copy{font-size:14px;line-height:1.75;max-width:790px}
.read-more{display:inline-flex;align-items:center;gap:12px;font-family:"Cinzel",Georgia,serif;font-size:15px;margin-top:18px;white-space:nowrap}

/* Why */
.why{height:424px;text-align:center;padding-top:78px}
.section-title{font-family:"Cinzel",Georgia,serif;font-size:38px;font-weight:400;color:var(--ink)}
.why-copy{width:800px;margin:22px auto 0;font-size:14px;line-height:1.75;color:var(--muted)}
.chevrons{margin-top:28px}

/* Services */
.services{height:1128px;position:relative;text-align:center}
.services .section-title{padding-top:10px}
.service-grid{position:absolute;left:80px;top:90px;width:1040px;display:grid;grid-template-columns:520px 520px;grid-auto-rows:300px;row-gap:10px}
.service-photo{width:100%;height:100%}
.service-card{border:1px solid #ddd;background:var(--white);display:flex;flex-direction:column;align-items:center;justify-content:center;padding:0 60px}
.service-card h3{font-family:"Cinzel",Georgia,serif;font-size:24px;font-weight:400;color:var(--green);margin:10px 0 12px}
.service-card p{font-size:14px;line-height:1.7;color:var(--muted)}
.service-card .read-more{color:var(--ink);margin-top:12px;align-self:flex-end}
.scroll-down{position:absolute;left:581px;top:1046px}

/* Video band */
.video-band{height:333px;color:var(--white);text-align:center;padding-top:80px;background:
  radial-gradient(ellipse 300px 180px at 200px 120px,rgba(140,180,90,.55),transparent 70%),
  radial-gradient(ellipse 320px 200px at 960px 200px,rgba(120,160,70,.5),transparent 70%),
  linear-gradient(120deg,#2c5a18 0%,#4a7a2c 40%,#3c6a22 65%,#264d12 100%)}
.video-band h2{font-family:"Cinzel",Georgia,serif;font-size:38px;font-weight:400;margin:20px 0 12px}
.video-band p{font-size:14px;line-height:1.6;width:620px;margin:0 auto}

/* Team */
.team{height:645px;text-align:center;padding-top:60px}
.team-intro{width:720px;margin:18px auto 0;font-size:14px;line-height:1.7;color:var(--muted)}
.team-grid{display:flex;justify-content:space-between;width:1040px;margin:34px auto 0}
.team-card{width:304px;height:367px;background:var(--slate);color:var(--white);display:flex;flex-direction:column;align-items:center;padding-top:30px;position:relative}
.team-card.featured{background:var(--green)}
.team-photo{width:120px;height:120px;border-radius:50%;border:4px solid var(--white);background:
  radial-gradient(circle at 50% 42%,#d9b89c 0,#b48a6c 30%,transparent 44%),
  linear-gradient(160deg,#e4e0d8,#8a847c 60%,#4a4640)}
.team-name{font-family:"Cinzel",Georgia,serif;font-size:19px;margin-top:20px}
.team-role{font-size:13px;line-height:1.5;margin-top:8px;width:190px}
.socials{display:flex;gap:10px;margin-top:14px}
.social{width:32px;height:32px;border-radius:50%;background:var(--white);display:block}
.team-card .view-profile{position:absolute;left:0;right:0;bottom:0;height:47px;background:var(--grey-bar);font-family:"Cinzel",Georgia,serif;font-size:18px;line-height:47px}
.team-card.featured .view-profile{background:var(--green-mid)}

/* Testimonials */
.testimonials{height:471px;text-align:center;padding-top:66px;background:
  radial-gradient(ellipse 260px 200px at 150px 300px,rgba(255,255,230,.6),transparent 70%),
  radial-gradient(ellipse 300px 220px at 1050px 120px,rgba(120,170,50,.55),transparent 70%),
  linear-gradient(120deg,#dcefb6 0%,#9bcf5e 45%,#c6e691 70%,#7fb843 100%)}
.testimonial-grid{display:flex;justify-content:space-between;width:1040px;margin:54px auto 0}
.testimonial{width:251px;height:218px;background:var(--green-dark);color:var(--white);position:relative;padding:52px 20px 0;font-size:13px;line-height:1.6}
.testimonial.slate{background:#2e3540}
.badge{position:absolute;left:70px;top:-30px;width:110px;height:52px;background:var(--white);border-radius:4px}
.testimonial .read-more{position:absolute;left:0;right:0;bottom:16px;justify-content:center;font-size:14px;color:var(--white)}

/* Blog */
.blog{height:527px;text-align:center;padding-top:60px}
.blog-grid{display:flex;justify-content:space-between;width:1040px;margin:22px auto 0;text-align:left}
.post{width:323px}
.post-thumb{position:relative;height:209px}
.post-thumb .photo{width:100%;height:100%}
.post-date{position:absolute;left:0;top:0;width:74px;height:77px;background:var(--green);color:var(--white);text-align:center;padding-top:10px;font-size:13px}
.post-date b{display:block;font-size:26px;line-height:1.1}
.post h3{font-family:"Cinzel",Georgia,serif;font-size:19px;font-weight:700;color:var(--green-dark);margin-top:26px;white-space:nowrap}
.post p{font-size:13.5px;line-height:1.6;color:var(--muted);margin-top:8px}

/* Footer */
.site-footer{height:353px;background:var(--footer);color:var(--white);display:flex;padding:52px 0 0 110px;font-size:13.5px;line-height:1.6}
.footer-col h4{font-family:"Cinzel",Georgia,serif;font-size:19px;font-weight:400;margin-bottom:12px}
.footer-about{width:277px}
.footer-about .brand-name{font-size:24px}
.footer-about .brand-tag{font-size:11px;margin-bottom:10px}
.footer-about p{width:220px}
.footer-about .socials{margin-top:20px}
.footer-links{width:218px}
.footer-links li{list-style:none;display:flex;align-items:center;gap:8px}
.footer-links li::before{content:"";width:6px;height:6px;background:var(--white);display:block}
.footer-contact{width:262px}
.contact-row{display:flex;gap:12px;align-items:flex-start;margin-bottom:10px}
.contact-row svg{flex:none;margin-top:3px}
.footer-news{width:250px}
.news-input{margin-top:14px;width:240px;height:40px;background:var(--white);color:#999;font-size:13px;padding:10px 12px}
.btn-subscribe{display:inline-block;margin-top:14px;background:var(--green-light);color:var(--ink);font-family:"Cinzel",Georgia,serif;font-size:16px;padding:8px 14px}
.copyright{height:69px;background:var(--footer-dark);color:var(--white);text-align:center;font-size:13px;line-height:69px}
</style>
</head>
<body>

<section class="hero">
  <div class="hero-photo photo" role="img" aria-label="Bright gym with people running on treadmills"></div>
  <header class="site-header">
    <div>
      <div class="brand-name">Morval Pastime</div>
      <div class="brand-tag">Health, Wellness, Fitness, Consultants</div>
    </div>
    <nav class="main-nav">
      <a class="active" href="#">Home</a><a href="#">Contact</a><a href="#">Our Team</a><a href="#">Testimonials</a><a href="#">Health</a><a href="#">Wellness</a><a href="#">Fitness</a><a href="#">Brisk Rig</a>
    </nav>
  </header>
  <div class="hero-panel">
    <div class="hero-kicker">
      <svg width="34" height="14" viewBox="0 0 34 14"><rect x="0" y="2" width="5" height="10" fill="#fff"/><rect x="5" y="5" width="24" height="4" fill="#fff"/><rect x="29" y="2" width="5" height="10" fill="#fff"/></svg>
      Health-Wellness-fitness
      <svg width="34" height="14" viewBox="0 0 34 14"><rect x="0" y="2" width="5" height="10" fill="#fff"/><rect x="5" y="5" width="24" height="4" fill="#fff"/><rect x="29" y="2" width="5" height="10" fill="#fff"/></svg>
    </div>
    <h1 class="hero-title">Morval Pastime</h1>
    <p class="hero-text">Lorem Ipsum is simply dummy text of the printing and typesetting industry.</p>
    <a class="btn-contact" href="#">Contact Us</a>
  </div>
</section>

<section class="about">
  <h2>About Morval Pastime</h2>
  <div class="about-body">
    <div class="about-photo photo" role="img" aria-label="Portrait of the founder"></div>
    <div>
      <div class="about-name">Owen Prady</div>
      <div class="about-role">Founder / Director - Morval Pastime</div>
      <p class="about-copy">Morval Pastime long term success depends on the talents commitment and shared values of our people. Morval Pastime is made of a unique hand picked team that will ensure the best possible service is delivered, as a company were passionate about delivering the best for our clients so we employ and partner with the best people who share that drive, passion and are led through the Morval values in everything they do.</p>
      <a class="read-more" href="#">Read More <svg width="30" height="10" viewBox="0 0 30 10"><path d="M0 5H27M22 1l5 4-5 4" stroke="#fff" stroke-width="2" fill="none"/></svg></a>
    </div>
  </div>
</section>

<section class="why">
  <h2 class="section-title">Why Choose Morval Pastime?</h2>
  <p class="why-copy">Morval Pastime are leading consultants to the Health, Wellness and Fitness industry, with over 25 years experience working with some of the biggest global worldwide brands from equipment providers and facility operators to mass participation events and obstacle course races. Morval Pastime is a multi disciplined business specialising in helping brands grow through insight, strategy creation and valuable sector collaboration, recent clients include the exclusive distribution of Brisk Rig bodyweight training products for the UK and Ireland.</p>
  <svg class="chevrons" width="60" height="34" viewBox="0 0 60 34"><path d="M2 3l28 14L58 3M2 16l28 14 28-14" stroke="#2f6812" stroke-width="3" fill="none"/></svg>
</section>

<section class="services">
  <h2 class="section-title">What can you do?</h2>
  <div class="service-grid">
    <div class="service-photo photo" role="img" aria-label="Women exercising with resistance bands in a studio" style="background:radial-gradient(ellipse 180px 200px at 360px 180px,rgba(240,220,60,.85),transparent 70%),radial-gradient(ellipse 120px 160px at 470px 120px,rgba(200,30,30,.9),transparent 75%),linear-gradient(120deg,#eae6dc 0%,#d9c25a 35%,#c0392b 70%,#8a1d16 100%)"></div>
    <div class="service-card">
      <svg width="60" height="44" viewBox="0 0 60 44"><path d="M30 42C10 28 2 20 2 12 2 5 8 1 14 1c7 0 12 5 16 10C34 6 39 1 46 1c6 0 12 4 12 11 0 8-8 16-28 30z" fill="none" stroke="#2f6812" stroke-width="3"/><path d="M8 22h12l4-8 6 14 4-6h18" fill="none" stroke="#2f6812" stroke-width="3"/></svg>
      <h3>Health</h3>
      <p>Lorem Ipsum is simply dummy text of the printing and typesetting industry. Lorem Ipsum has been the industry's standard dummy text ever since the 1500s, when an unknown printer took a galley.</p>
      <a class="read-more" href="#">Read More <svg width="30" height="10" viewBox="0 0 30 10"><path d="M0 5H27M22 1l5 4-5 4" stroke="#222" stroke-width="2" fill="none"/></svg></a>
    </div>
    <div class="service-card">
      <svg width="54" height="54" viewBox="0 0 54 54"><circle cx="27" cy="27" r="8" fill="none" stroke="#2f6812" stroke-width="3"/><g fill="#2f6812"><circle cx="27" cy="5" r="3"/><circle cx="27" cy="49" r="3"/><circle cx="5" cy="27" r="3"/><circle cx="49" cy="27" r="3"/><circle cx="11" cy="11" r="3"/><circle cx="43" cy="43" r="3"/><circle cx="43" cy="11" r="3"/><circle cx="11" cy="43" r="3"/></g></svg>
      <h3>Wellness</h3>
      <p>Lorem Ipsum is simply dummy text of the printing and typesetting industry. Lorem Ipsum has been the industry's standard dummy text ever since the 1500s, when an unknown printer took a galley.</p>
      <a class="read-more" href="#">Read More <svg width="30" height="10" viewBox="0 0 30 10"><path d="M0 5H27M22 1l5 4-5 4" stroke="#222" stroke-width="2" fill="none"/></svg></a>
    </div>
    <div class="service-photo photo" role="img" aria-label="Older adults on rowing machines in a gym" style="background:radial-gradient(ellipse 160px 140px at 140px 170px,rgba(90,60,40,.85),transparent 70%),radial-gradient(ellipse 160px 160px at 380px 150px,rgba(200,60,60,.55),transparent 70%),linear-gradient(180deg,#eef0ee 0%,#c9c4b8 45%,#8a8f6a 80%,#5c6a3a 100%)"></div>
    <div class="service-photo photo" role="img" aria-label="Group of people smiling after a workout" style="background:radial-gradient(ellipse 140px 180px at 300px 200px,rgba(40,40,48,.85),transparent 70%),radial-gradient(ellipse 120px 160px at 110px 160px,rgba(70,80,110,.7),transparent 70%),linear-gradient(180deg,#f2f2f0 0%,#d8d6d0 40%,#7a7f8a 80%,#3c4050 100%)"></div>
    <div class="service-card">
      <svg width="56" height="40" viewBox="0 0 56 40"><rect x="2" y="10" width="8" height="20" fill="#2f6812"/><rect x="12" y="5" width="8" height="30" fill="#2f6812"/><rect x="20" y="17" width="16" height="6" fill="#2f6812"/><rect x="36" y="5" width="8" height="30" fill="#2f6812"/><rect x="46" y="10" width="8" height="20" fill="#2f6812"/></svg>
      <h3>Fitness</h3>
      <p>Lorem Ipsum is simply dummy text of the printing and typesetting industry. Lorem Ipsum has been the industry's standard dummy text ever since the 1500s, when an unknown printer took a galley.</p>
      <a class="read-more" href="#">Read More <svg width="30" height="10" viewBox="0 0 30 10"><path d="M0 5H27M22 1l5 4-5 4" stroke="#222" stroke-width="2" fill="none"/></svg></a>
    </div>
  </div>
  <svg class="scroll-down" width="38" height="38" viewBox="0 0 38 38"><circle cx="19" cy="19" r="19" fill="#1e4a0c"/><path d="M19 10v17M12 20l7 7 7-7" stroke="#fff" stroke-width="3" fill="none"/></svg>
</section>

<section class="video-band" role="img" aria-label="Green tinted photo of people training in a gym">
  <svg width="60" height="60" viewBox="0 0 60 60"><circle cx="30" cy="30" r="30" fill="#fff"/><path d="M24 17l20 13-20 13z" fill="#2f6812"/></svg>
  <h2>The Bodyweight circuit for Every Body</h2>
  <p>Lorem Ipsum is simply dummy text of the printing and typesetting industry. Lorem Ipsum has been the industry's standard dummy text ever since the 1500s, when an unknown printer took a galley.</p>
</section>

<section class="team">
  <h2 class="section-title">Our Team</h2>
  <p class="team-intro">Lorem Ipsum is simply dummy text of the printing and typesetting industry. Lorem Ipsum has been the industry's standard dummy text ever since the 1500s, when an unknown printer took a galley.</p>
  <div class="team-grid">
    <article class="team-card">
      <div class="team-photo photo" role="img" aria-label="Team member portrait"></div>
      <div class="team-name">Harlow</div>
      <div class="team-role">A leading life coach,self development guru</div>
      <div class="socials"><span class="social"></span><span class="social"></span><span class="social"></span><span class="social"></span></div>
      <a class="view-profile" href="#">View Profile</a>
    </article>
    <article class="team-card featured">
      <div class="team-photo photo" role="img" aria-label="Team member portrait"></div>
      <div class="team-name">Callum Brisby</div>
      <div class="team-role">Founder and owner of Grindworks</div>
      <div class="socials"><span class="social"></span><span class="social"></span><span class="social"></span><span class="social"></span></div>
      <a class="view-profile" href="#">View Profile</a>
    </article>
    <article class="team-card">
      <div class="team-photo photo" role="img" aria-label="Team member portrait"></div>
      <div class="team-name">Dane Purcell</div>
      <div class="team-role">A Powerhouse of fitness knowledge</div>
      <div class="socials"><span class="social"></span><span class="social"></span><span class="social"></span><span class="social"></span></div>
      <a class="view-profile" href="#">View Profile</a>
    </article>
  </div>
</section>

<section class="testimonials" role="img" aria-label="Soft green tinted photo of a fitness class">
  <h2 class="section-title">Testimonial</h2>
  <div class="testimonial-grid">
    <article class="testimonial slate">
      <span class="badge"></span>
      <p>Working alongside the Morval Pastime &amp; Vale Active team with the Weight Loss Challenge at Brookmere Hospital has been...</p>
      <a class="read-more" href="#">Read More <svg width="30" height="10" viewBox="0 0 30 10"><path d="M0 5H27M22 1l5 4-5 4" stroke="#fff" stroke-width="2" fill="none"/></svg></a>
    </article>
    <article class="testimonial">
      <span class="badge" style="border-radius:50%;width:56px;left:98px"></span>
      <p>Kestrel Dash Race and Morval Pastime first collaborated in 2015. Owen and the Morval team have showed impeccable...</p>
      <a class="read-more" href="#">Read More <svg width="30" height="10" viewBox="0 0 30 10"><path d="M0 5H27M22 1l5 4-5 4" stroke="#fff" stroke-width="2" fill="none"/></svg></a>
    </article>
    <article class="testimonial">
      <span class="badge"></span>
      <p>Working alongside the Morval Pastime &amp; Vale Active team with the Weight Loss Challenge at Brookmere Hospital has been...</p>
      <a class="read-more" href="#">Read More <svg width="30" height="10" viewBox="0 0 30 10"><path d="M0 5H27M22 1l5 4-5 4" stroke="#fff" stroke-width="2" fill="none"/></svg></a>
    </article>
    <article class="testimonial">
      <span class="badge"></span>
      <p>Pinnacle Fitness has utilised the in depth, health, wellness and fitness industry knowledge and expertise that Owen...</p>
      <a class="read-more" href="#">Read More <svg width="30" height="10" viewBox="0 0 30 10"><path d="M0 5H27M22 1l5 4-5 4" stroke="#fff" stroke-width="2" fill="none"/></svg></a>
    </article>
  </div>
</section>

<section class="blog">
  <h2 class="section-title">Latest Blog Post</h2>
  <div class="blog-grid">
    <article class="post">
      <div class="post-thumb"><div class="photo" role="img" aria-label="Man training with a cable machine" style="background:radial-gradient(ellipse 90px 110px at 200px 110px,rgba(40,40,40,.85),transparent 70%),linear-gradient(120deg,#3a3a3a 0%,#9a8f80 45%,#e4e0d8 75%,#b8b0a4 100%)"></div><div class="post-date"><b>11</b>Oct</div></div>
      <h3>Lorem Ipsum is simply dummy</h3>
      <p>Lorem Ipsum is simply dummy text of the printing and typesetting industry. Lorem Ipsum has been the industry's standard dummy text...</p>
    </article>
    <article class="post">
      <div class="post-thumb"><div class="photo" role="img" aria-label="Person lifting weights in a gym" style="background:radial-gradient(ellipse 100px 110px at 150px 120px,rgba(150,100,70,.8),transparent 70%),linear-gradient(120deg,#d6d0c6 0%,#8a7a68 45%,#4a3e34 75%,#2d2d2d 100%)"></div><div class="post-date"><b>11</b>Oct</div></div>
      <h3>Lorem Ipsum is simply dummy</h3>
      <p>Lorem Ipsum is simply dummy text of the printing and typesetting industry. Lorem Ipsum has been the industry's standard dummy text...</p>
    </article>
    <article class="post">
      <div class="post-thumb"><div class="photo" role="img" aria-label="Athlete doing bodyweight exercise" style="background:radial-gradient(ellipse 120px 90px at 180px 130px,rgba(30,30,30,.85),transparent 70%),linear-gradient(120deg,#2a2a2a 0%,#7a7066 40%,#cfc6b8 75%,#9a9184 100%)"></div><div class="post-date"><b>11</b>Oct</div></div>
      <h3>Lorem Ipsum is simply dummy</h3>
      <p>Lorem Ipsum is simply dummy text of the printing and typesetting industry. Lorem Ipsum has been the industry's standard dummy text...</p>
    </article>
  </div>
</section>

<footer class="site-footer">
  <div class="footer-col footer-about">
    <div class="brand-name">Morval Pastime</div>
    <div class="brand-tag">Health, Wellness, Fitness, Consultants</div>
    <p>Lorem Ipsum is simply dummy text of the printing and typesetting industry. Lorem Ipsum has been the industry's standard dummy text ever since the.</p>
    <div class="socials"><span class="social"></span><span class="social"></span><span class="social"></span></div>
  </div>
  <div class="footer-col footer-links">
    <h4>Useful Link</h4>
    <ul>
      <li>Home</li><li>Contact</li><li>Our Team</li><li>Testimonial</li><li>Health</li><li>Wellness</li><li>Fitness</li><li>Brisk Rig</li>
    </ul>
  </div>
  <div class="footer-col footer-contact">
    <h4>Contact Us</h4>
    <div class="contact-row"><svg width="14" height="18" viewBox="0 0 14 18"><path d="M7 0a7 7 0 0 0-7 7c0 5 7 11 7 11s7-6 7-11a7 7 0 0 0-7-7z" fill="#fff"/><circle cx="7" cy="7" r="2.5" fill="#1c4409"/></svg><span>Morval Pastime<br>The Larches Harwick<br>UK &amp; Ireland</span></div>
    <div class="contact-row"><svg width="16" height="16" viewBox="0 0 16 16"><path d="M3 1l3 3-2 2c1 2 3 4 6 6l2-2 3 3-2 2C7 15 1 9 1 3z" fill="#fff"/></svg><span>07000-481620</span></div>
    <div class="contact-row"><svg width="16" height="12" viewBox="0 0 16 12"><rect width="16" height="12" fill="#fff"/><path d="M0 0l8 7 8-7" stroke="#1c4409" stroke-width="1.5" fill="none"/></svg><span>hello@morvalpastime.com</span></div>
    <div class="contact-row"><svg width="16" height="16" viewBox="0 0 16 16"><circle cx="8" cy="8" r="7" fill="none" stroke="#fff" stroke-width="1.5"/><path d="M1 8h14M8 1c-3 4-3 10 0 14M8 1c3 4 3 10 0 14" stroke="#fff" stroke-width="1.2" fill="none"/></svg><span>www.morvalpastime.com</span></div>
    <div class="contact-row"><svg width="16" height="16" viewBox="0 0 16 16"><circle cx="8" cy="8" r="7" fill="#fff"/></svg><span>Morvalpastime</span></div>
  </div>
  <div class="footer-col footer-news">
    <h4>Newsletter</h4>
    <p>Would you like to receive exclusive access to articles, white papers and our regular monthly newsletter?</p>
    <div class="news-input">Enter Email Id</div>
    <a class="btn-subscribe" href="#">Subscribe</a>
  </div>
</footer>
<div class="copyright">Copyright © 2017 MORVAL PASTIME. All Rights Reserved.</div>

</body>
</html>
```